Home page redesign for an international job board

Need a modern design based on current structure of the page. I am happy with the current structure and layout/architecture, not entirely happy with how it looks. While I still want to keep most of the elements in place ( especially the search box) I would like to get another look and feel - more appealing to any audience related to online job search

Home page is: www.lucrubrisa.ro

Target Market(s)

job seeekers and employers

Industry/Entity Type

Architecture

Number of Pages Required

1 page

Font styles to use
Sans Serif

Colors
33a6d7

Requirements
Must have
• Stay with the same structure: Seach box, latest jobs, articles
Nice to have
• Key element: search for jobs - this needs to be very clear

```html
<!DOCTYPE html>
<html lang="en">
<head>
<meta charset="utf-8">
<title>LucruBrisa – Home</title>
<link href="https://fonts.googleapis.com/css2?family=Open+Sans:wght@400;600;700&family=Raleway:wght@400;500;600&display=swap" rel="stylesheet">
<style>
:root{
  --red:#c40e14;
  --red-dark:#a80b10;
  --ink:#333;
  --muted:#555;
  --white:#fff;
  --header-grey:#5d5d5f;
  --panel:rgba(110,108,110,.72);
  --light:#e4e4e4;
  --card:#3a3a3a;
}
*{box-sizing:border-box;margin:0;padding:0}
html,body{width:1200px;height:2269px;overflow:hidden}
body{font-family:"Open Sans",sans-serif;color:var(--ink);background:var(--white)}
.page{position:relative;width:1200px;height:2269px;overflow:hidden}
.abs{position:absolute}
a{color:inherit;text-decoration:none}

/* top bar */
.topbar{left:0;top:0;width:1200px;height:46px;background:var(--red)}
.toplinks{right:52px;top:14px;font-size:12px;color:var(--white)}
.toplinks span{margin:0 5px}

/* hero */
.hero-photo{left:0;top:46px;width:1200px;height:691px;background:linear-gradient(100deg,#6a6767 0%,#7b7778 35%,#8c8a8b 60%,#9a9a9c 100%)}
.hero-line{left:0;top:145px;width:1200px;height:1px;background:rgba(255,255,255,.35)}
.brand{left:52px;top:86px;width:240px;height:60px;background:var(--white);display:flex;align-items:center;padding-left:22px;gap:10px}
.brand-dot{width:30px;height:30px;border-radius:50%;background:var(--red)}
.brand-name{font-family:"Open Sans",sans-serif;font-size:23px;font-weight:400;color:#3a3a3a}
.nav{top:91px;font-size:12px;color:var(--white);text-transform:uppercase}
.nav-active{left:321px;top:83px;width:90px;height:31px;background:var(--red);color:var(--white);font-size:11.5px;display:flex;align-items:center;justify-content:center}
.login{left:1054px;top:90px;font-size:12px;color:var(--white)}

/* search panel */
.search{left:614px;top:146px;width:541px;height:508px;background:var(--panel)}
.search-head{left:614px;top:146px;width:541px;height:66px;background:var(--red);color:var(--white);font-family:"Raleway",sans-serif;font-size:23px;font-weight:600;display:flex;align-items:center;justify-content:center}
.field-label{width:160px;text-align:right;left:588px;font-family:"Raleway",sans-serif;font-size:17px;color:var(--white)}
.field{left:819px;width:305px;height:33px;border:1px solid rgba(255,255,255,.75);background:rgba(120,118,120,.4)}
.field svg{position:absolute;right:15px;top:13px}
.btn-search{left:818px;top:508px;width:308px;height:43px;background:var(--red);color:var(--white);font-size:15px;display:flex;align-items:center;justify-content:center}
.tool{background:var(--white);display:flex;flex-direction:column;align-items:center;justify-content:center;color:#444;font-size:9px;text-align:center;line-height:13px;text-transform:uppercase}

/* latest jobs */
.jobs-bg{left:0;top:737px;width:1200px;height:265px;background:linear-gradient(90deg,#dcdcdc,#e8e8e8 50%,#dedede)}
.job-circle{width:124px;height:124px;border-radius:50%;background:var(--red);border:3px solid var(--white);box-shadow:0 0 0 2px var(--red);display:flex;align-items:center;justify-content:center}
.job-circle.first{background:var(--white);box-shadow:0 0 0 2px var(--red)}
.job{width:360px;text-align:center}
.job-title{font-size:17px;font-weight:600;color:var(--red);letter-spacing:1px;text-transform:uppercase}
.job-co{font-size:12px;color:#555;line-height:17px;margin-top:19px}
.job-more{font-size:12px;margin-top:17px;color:#222;text-transform:uppercase}
.job-more.hot{color:var(--red)}

/* article slider */
.slider{left:0;top:1002px;width:1200px;height:245px;background:var(--red)}
.article-img{left:277px;top:1045px;width:308px;height:164px;background:linear-gradient(135deg,#2b3440,#55606e 50%,#9aa3ad)}
.article-title{left:626px;top:1045px;font-family:"Raleway",sans-serif;font-size:18px;color:var(--white);letter-spacing:-.3px}
.article-text{left:627px;top:1080px;width:314px;font-family:"Raleway",sans-serif;font-size:12px;line-height:17px;color:var(--white);text-align:justify}
.meta-date{left:627px;top:1172px;width:129px;height:29px;background:#2a2a2a;color:var(--white);font-size:10px;display:flex;align-items:center;justify-content:center}
.meta-comment{left:763px;top:1180px;font-size:10.5px;color:var(--white);display:flex;align-items:center;gap:6px}
.meta-share{top:1177px;width:20px;height:20px}

/* services */
.service-bg{left:0;top:1247px;width:1200px;height:558px;background:linear-gradient(180deg,#7c7d80,#8b8c8f 45%,#76777a)}
.service-title{left:0;top:1295px;width:1200px;text-align:center;font-family:"Raleway",sans-serif;font-size:35px;font-weight:500;color:var(--white)}
.service-intro{left:100px;top:1361px;width:1000px;text-align:center;font-size:12px;line-height:21px;color:var(--white)}
.app-tile{top:1437px;width:342px;height:198px;background:var(--card);display:flex;align-items:center;justify-content:center;color:var(--white);font-size:40px;font-weight:600}
.app-label{top:1647px;width:342px;height:36px;background:var(--white);color:var(--red);font-size:15px;font-weight:600;padding-left:12px;display:flex;align-items:center;text-transform:uppercase}
.app-text{top:1692px;width:350px;font-size:12.5px;line-height:18px;color:var(--white)}
.app-btn{top:1735px;width:96px;height:33px;border:1px solid var(--white);background:#2e2e2e;color:var(--white);font-size:12px;display:flex;align-items:center;justify-content:center}
.app-btn.hot{background:var(--red)}

/* footer links */
.footer{left:0;top:1805px;width:1200px;height:241px;background:#ececec}
.col-head{top:1843px;font-size:17px;font-weight:600;color:var(--red)}
.col-list{top:1886px;list-style:none;font-size:12px;color:#333;line-height:21px}
.col-list li::before{content:"›";margin-right:9px;font-size:14px}
.col-rule{top:1838px;width:1px;height:150px;background:#dadada}
.partner{left:956px;top:1876px;width:163px;height:113px;background:#dfdfe0}

/* browse */
.browse{left:0;top:2046px;width:1200px;height:151px;background:#dcdcdc}
.browse-head{left:0;top:2088px;width:1200px;text-align:center;font-size:15px;font-weight:600;color:var(--red)}
.browse-line{left:0;width:1200px;text-align:center;font-size:12px;color:#333}
.browse-line b{font-weight:400;color:var(--red);font-size:13px}

/* bottom */
.bottom{left:0;top:2197px;width:1200px;height:72px;background:var(--red);color:var(--white)}
.copy{left:51px;top:2228px;font-size:10px;color:var(--white)}
.legal{left:420px;top:2224px;width:470px;text-align:center;font-size:10px;color:var(--white)}
.social-dot{top:2228px;width:14px;height:14px;border-radius:50%;background:var(--white)}
</style>
</head>
<body>
<div class="page">

  <!-- top bar -->
  <div class="abs topbar"></div>
  <div class="abs toplinks">Jobs<span>|</span>Career Coach<span>|</span>Interview Tips<span>|</span>Ro<span>|</span>En</div>

  <!-- hero -->
  <div class="abs hero-photo" role="img" aria-label="Photo of a woman using a tablet at a desk"></div>
  <div class="abs hero-line"></div>
  <div class="abs brand"><span class="brand-dot"></span><span class="brand-name">LucruBrisa</span></div>
  <div class="abs nav-active">SEARCH JOBS</div>
  <div class="abs nav" style="left:450px">My Account</div>
  <div class="abs nav" style="left:572px">Career Counselling</div>
  <div class="abs nav" style="left:745px">Features</div>
  <div class="abs nav" style="left:846px">Employer &amp; Post a Job</div>
  <div class="abs login">LOGIN | REGISTER</div>

  <!-- search -->
  <div class="abs search"></div>
  <div class="abs search-head">SEARCH JOBS</div>

  <div class="abs field-label" style="top:263px">Keywords</div>
  <div class="abs field" style="top:258px"></div>
  <div class="abs field-label" style="top:312px">Classification</div>
  <div class="abs field" style="top:307px"><svg width="11" height="7"><path d="M0 0h11L5.5 7z" fill="#fff"/></svg></div>
  <div class="abs field-label" style="top:361px">Region</div>
  <div class="abs field" style="top:356px"><svg width="11" height="7"><path d="M0 0h11L5.5 7z" fill="#fff"/></svg></div>
  <div class="abs field-label" style="top:413px">Work Type</div>
  <div class="abs field" style="top:408px"><svg width="11" height="7"><path d="M0 0h11L5.5 7z" fill="#fff"/></svg></div>
  <div class="abs field-label" style="top:458px">Locatie</div>
  <div class="abs field" style="top:453px"><svg width="11" height="7"><path d="M0 0h11L5.5 7z" fill="#fff"/></svg></div>

  <div class="abs btn-search">SEARCH</div>
  <div class="abs tool" style="left:818px;top:559px;width:96px;height:47px">
    <svg width="32" height="24" viewBox="0 0 32 24"><rect x="2" y="2" width="18" height="20" fill="none" stroke="#c40e14" stroke-width="2"/><path d="M6 8h10M6 12h10M6 16h6" stroke="#c40e14" stroke-width="2"/><path d="M17 19l10-12 3 3-10 12h-3z" fill="#c40e14"/></svg>
  </div>
  <div class="abs tool" style="left:925px;top:559px;width:96px;height:70px">
    <svg width="22" height="22" viewBox="0 0 22 22"><circle cx="11" cy="12" r="8" fill="none" stroke="#c40e14" stroke-width="2"/><path d="M11 8v4l3 2" stroke="#c40e14" stroke-width="2" fill="none"/><path d="M2 5l4-3M20 5l-4-3" stroke="#c40e14" stroke-width="2"/></svg>
    <span style="margin-top:3px">Set your<br>job alerts</span>
  </div>
  <div class="abs tool" style="left:1036px;top:559px;width:90px;height:46px">
    <svg width="20" height="20" viewBox="0 0 20 20"><circle cx="8" cy="8" r="6" fill="none" stroke="#c40e14" stroke-width="3"/><path d="M12.5 12.5l5 5" stroke="#c40e14" stroke-width="3.5" stroke-linecap="round"/></svg>
  </div>

  <!-- latest jobs -->
  <div class="abs jobs-bg" role="img" aria-label="Faded photo of an office desk"></div>

  <div class="abs job-circle first" style="left:190px;top:675px">
    <svg width="40" height="40"><rect x="4" y="4" width="32" height="32" fill="#c40e14"/></svg>
  </div>
  <div class="abs job-circle" style="left:548px;top:675px">
    <svg width="50" height="54" viewBox="0 0 50 54"><circle cx="25" cy="15" r="12" fill="#fff"/><path d="M3 54c0-16 9-24 22-24s22 8 22 24z" fill="#fff"/></svg>
  </div>
  <div class="abs job-circle" style="left:869px;top:675px">
    <svg width="44" height="54" viewBox="0 0 44 54"><rect x="2" y="2" width="40" height="52" fill="#fff"/><g fill="#c40e14"><rect x="9" y="9" width="5" height="5"/><rect x="19" y="9" width="5" height="5"/><rect x="29" y="9" width="5" height="5"/><rect x="9" y="19" width="5" height="5"/><rect x="19" y="19" width="5" height="5"/><rect x="29" y="19" width="5" height="5"/><rect x="9" y="29" width="5" height="5"/><rect x="19" y="29" width="5" height="5"/><rect x="29" y="29" width="5" height="5"/><rect x="17" y="40" width="10" height="14"/></g></svg>
  </div>

  <div class="abs job" style="left:78px;top:816px">
    <div class="job-title">Java Developer</div>
    <div class="job-co">Ulm Vantor Engineering GmbH<br>Vantor Engineering GmbH</div>
    <div class="job-more hot">Read more ▸</div>
  </div>
  <div class="abs job" style="left:430px;top:817px">
    <div class="job-title">Jr. Developer</div>
    <div class="job-co">Atlanta, GA Meridia Network Solutions, Inc<br>Meridia Network Solutions, Inc</div>
    <div class="job-more">Read more ▸</div>
  </div>
  <div class="abs job" style="left:756px;top:816px">
    <div class="job-title">Digital Project Manager</div>
    <div class="job-co">Amsterdam Kestrel Bond Ltd<br>Kestrel Bond Ltd</div>
    <div class="job-more">Read more ▸</div>
  </div>

  <!-- article slider -->
  <div class="abs slider"></div>
  <svg class="abs" style="left:104px;top:1097px" width="40" height="40" viewBox="0 0 40 40"><path d="M40 0L0 20l40 20-12-20z" fill="#fff"/></svg>
  <svg class="abs" style="left:1048px;top:1097px" width="40" height="40" viewBox="0 0 40 40"><path d="M0 0l40 20L0 40l12-20z" fill="#fff"/></svg>
  <div class="abs article-img" role="img" aria-label="Photo of a woman with a tablet in front of a night city skyline"></div>
  <div class="abs article-title">Invatarea, Continua pe tot Parcursul Vietii</div>
  <div class="abs article-text">Lorem ipsum dolor sit amet, consectetur adipiscing elit, sed do eiusmod tempor incididunt ut labore et dolore magna aliqua.Lorem ipsum dolor sit amet, consectetur adipiscing elit, sed do eiusmod tempor incididunt</div>
  <div class="abs meta-date">Posted by : 20-Aug-2015</div>
  <div class="abs meta-comment"><svg width="14" height="11"><ellipse cx="6" cy="5" rx="6" ry="4.5" fill="#f2b01e"/></svg>Comment :3</div>
  <div class="abs meta-share" style="left:859px;background:#1c5f93"></div>
  <div class="abs meta-share" style="left:889px;background:#2aa3e0"></div>
  <div class="abs meta-share" style="left:917px;background:#2f57a6"></div>

  <!-- services -->
  <div class="abs service-bg" role="img" aria-label="Faded photo of a laptop and keyboard on a desk"></div>
  <div class="abs service-title">Our Service</div>
  <div class="abs service-intro">Lorem ipsum dolor sit amet, consectetur adipiscing elit, sed do eiusmod tempor incididunt ut labore et dolore magna aliqua. Ut enim ad minim veniam, quis nostrud exercitation ullam-co laboris. Duis aute irure dolor in reprehenderit in voluptate velit esse cillum dolore eu fugiat nulla pariatur.</div>

  <div class="abs app-tile" style="left:49px">PearPhone</div>
  <div class="abs app-tile" style="left:433px">Droidex</div>
  <div class="abs app-tile" style="left:812px">Friendbook</div>

  <div class="abs app-label" style="left:50px">Job app for PearPhone</div>
  <div class="abs app-label" style="left:433px">Job app for Droidex</div>
  <div class="abs app-label" style="left:809px">Job app for Friendbook</div>

  <div class="abs app-text" style="left:49px">Lorem ipsum dolor sit amet, consectetur adipiscing elit, sed do eiusmod tempor incididunt</div>
  <div class="abs app-text" style="left:433px">Lorem ipsum dolor sit amet, consectetur adipiscing elit, sed do eiusmod tempor incididunt</div>
  <div class="abs app-text" style="left:812px">Lorem ipsum dolor sit amet, consectetur adipiscing elit, sed do eiusmod tempor incididunt</div>

  <div class="abs app-btn hot" style="left:48px">READ MORE</div>
  <div class="abs app-btn" style="left:432px">READ MORE</div>
  <div class="abs app-btn" style="left:811px">READ MORE</div>

  <!-- footer links -->
  <div class="abs footer"></div>
  <div class="abs col-head" style="left:47px">Connect with us</div>
  <ul class="abs col-list" style="left:49px"><li>Friendbook</li><li>Chirper</li><li>Orbit+</li><li>Workedin</li><li>Blog</li></ul>
  <div class="abs col-rule" style="left:224px"></div>
  <div class="abs col-head" style="left:261px">Go Mobile</div>
  <ul class="abs col-list" style="left:262px"><li>PearPhone App</li><li>Droidex App</li><li>Friendbook App</li><li>Mobile Version</li></ul>
  <div class="abs col-rule" style="left:433px"></div>
  <div class="abs col-head" style="left:492px">Employer Tools</div>
  <ul class="abs col-list" style="left:493px"><li>Post job ads</li><li>Access jobseekers</li><li>Resume Search</li><li>Analytics</li></ul>
  <div class="abs col-rule" style="left:667px"></div>
  <div class="abs col-head" style="left:730px">Job Seeker Tools</div>
  <ul class="abs col-list" style="left:729px"><li>Resume Posting</li><li>Job Alerts</li><li>Video Resume</li><li>Create Profile</li></ul>
  <div class="abs col-rule" style="left:905px"></div>
  <div class="abs col-head" style="left:978px">Our Partners</div>
  <div class="abs partner"></div>

  <!-- browse -->
  <div class="abs browse"></div>
  <div class="abs browse-head">Browse Jobs By</div>
  <div class="abs browse-line" style="top:2113px"><b>Classifications:</b> IT_Software Development | Banking | Sales | Medical | Engineering | view all classifications</div>
  <div class="abs browse-line" style="top:2136px"><b>Cities:</b> Bucuresti | Cluj-Napoca | Timisoara | Iasi | Constanta | Craiova | Brasov | Galati | Ploiesti | Oradea | Pitesti | Sibiu</div>

  <!-- bottom -->
  <div class="abs bottom"></div>
  <div class="abs copy">© All Rights Reserved. Copyrights @lucrubrisa. 2015</div>
  <div class="abs legal">About us | Terms and conditions | Privacy Policy | Contact</div>
  <svg class="abs" style="left:988px;top:2227px" width="14" height="14" viewBox="0 0 14 14"><circle cx="2.5" cy="11.5" r="2" fill="#fff"/><path d="M1 6a7 7 0 0 1 7 7M1 1a12 12 0 0 1 12 12" stroke="#fff" stroke-width="2" fill="none"/></svg>
  <div class="abs social-dot" style="left:1028px"></div>
  <div class="abs social-dot" style="left:1065px"></div>
  <div class="abs social-dot" style="left:1103px"></div>
  <div class="abs social-dot" style="left:1141px"></div>

</div>
</body>
</html>
```